Kerno Solutions: searching for a flyer to trow in letterboxes for properties we are interested in

Hello ,

Introduction:
We are a company based in Luxembourg called "Kerno Solutions". We are specialized in buying properties on which we develop and build constructions before selling them.

Informations for the flyer:
We need a flyer to trow into the letter boxes of property owners letting them know that we are interested in buying their property, if they are interested they can give us a call.

The text for the flyer/letter is in the attachment called >>2020-03-11_KS_Text for flyer,letter there might be slight changes<<.

We need to look competent, professional and financially stable.

The flyer needs to be short and not over welling with information otherwise it will land in the trash.

We have decided that we don't want real pictures on the flyer, but shapes of any kind, blue prints, drawings are fine.

Format should be in DIN A4. We plan to print the flyer on both sides in two different languages, in other words the design will be the same on both sides only the text will be in a different language.

I also added our current logo and here is the design of the website that is under construction at the moment http://www.kernosolutions-example.lu/. The logo's color can be changed into a different blue or uni color (all white or all black).
Updates

Hi, First time user the howl thing started faster as expected. Furthermore, I need to catch my boss to discust the project with him and he is on a lot of meetings. Please give us a little bit more time. Thanks

Target Market(s)

Property owners

Requirements
Must have
• email, phone number, tax number (RCS), Tax number , matriculation and address.
see word file in attachment for information
Nice to have
• Our company logo, in one form or an other, you can be creative, the logo is in the attachment.
Should not have
• Real pictures

```html
<!DOCTYPE html>
<html lang="fr">
<head>
<meta charset="utf-8">
<title>Kerno Solutions – Flyer</title>
<link href="https://fonts.googleapis.com/css2?family=Oswald:wght@600&family=Exo+2:wght@500&family=Lato:ital,wght@0,400;0,700;1,400&display=swap" rel="stylesheet">
<style>
  :root {
    --navy: #0b3d5c;
    --blue: #0a6291;
    --blue-mid: #10557f;
    --ice: #dcebf4;
    --pale: #a9cadb;
    --ink: #1f2a33;
    --white: #ffffff;
    --stage: #e6e8eb;
  }
  * { margin: 0; padding: 0; box-sizing: border-box; }
  html, body {
    width: 1200px; height: 1200px; overflow: hidden;
    background: var(--stage);
  }
  .flyer {
    position: absolute; left: 204px; top: 40px;
    width: 792px; height: 1120px;
    background: linear-gradient(180deg, var(--white) 0%, var(--white) 52%, var(--ice) 88%, var(--ice) 100%);
    box-shadow: 0 6px 24px rgba(0,0,0,.18);
    overflow: hidden;
    font-family: "Lato", sans-serif;
  }
  .header {
    position: absolute; left: 0; top: 0; width: 792px; height: 377px;
    background: linear-gradient(115deg, var(--navy) 0%, var(--blue-mid) 55%, var(--blue) 100%);
  }
  .header-notch { position: absolute; right: 0; top: 0; }
  .header-blueprint {
    position: absolute; left: 0; top: 0; width: 792px; height: 330px;
    background: radial-gradient(ellipse at 50% 50%, rgba(255,255,255,0) 30%, rgba(255,255,255,.06) 100%);
  }
  .header-brand {
    position: absolute; left: 0; top: 172px; width: 100%;
    text-align: center; color: var(--white);
    font-family: "Oswald", sans-serif; font-weight: 600;
    font-size: 40px; letter-spacing: .5px;
  }
  .header-brand .brand-mark {
    display: inline-block; width: 22px; height: 22px;
    background: var(--white); margin-right: 14px; vertical-align: 4px;
  }
  .tagline {
    position: absolute; left: 0; top: 286px; width: 100%;
    text-align: center; color: var(--white);
    font-family: "Exo 2", sans-serif; font-weight: 500;
  }
  .tagline .lead { font-size: 23px; text-transform: uppercase; line-height: 25px; }
  .tagline .sub { font-size: 21px; line-height: 25px; }
  .tagline-rule {
    width: 246px; margin: 9px auto 0;
    border-top: 2px dotted var(--white);
  }
  .letter { position: absolute; left: 33px; top: 412px; width: 730px; color: var(--ink); }
  .letter .salute { color: var(--blue); font-weight: 700; font-size: 17px; margin-bottom: 22px; }
  .letter p.body { font-style: italic; font-size: 16.6px; line-height: 23px; margin-bottom: 22px; }
  .letter .closing { font-weight: 700; font-size: 17px; margin-top: 45px; }
  .letter .signature { color: var(--blue); font-weight: 700; font-size: 17px; margin-top: 22px; }
  .footer-blueprint {
    position: absolute; left: 380px; top: 672px; width: 412px; height: 262px;
    background: linear-gradient(135deg, rgba(170,185,198,0) 0%, rgba(170,185,198,.22) 60%, rgba(170,185,198,.1) 100%);
  }
  .footer-brand {
    position: absolute; right: 30px; top: 896px;
    font-family: "Oswald", sans-serif; font-weight: 600;
    font-size: 31px; color: var(--navy); letter-spacing: .3px;
  }
  .footer-brand .brand-mark {
    display: inline-block; width: 16px; height: 16px;
    background: var(--navy); margin-right: 10px; vertical-align: 3px;
  }
  .footer-shapes { position: absolute; left: 0; top: 0; }
  .contact {
    position: absolute; left: 213px; top: 961px;
    color: var(--white); font-size: 16.5px; line-height: 21px;
  }
  .contact .company { font-weight: 700; padding-left: 24px; }
  .contact .row { display: flex; align-items: center; gap: 8px; }
  .contact svg { width: 16px; height: 16px; flex: none; }
  .website {
    position: absolute; left: 0; top: 1066px; width: 100%;
    display: flex; justify-content: center; align-items: center; gap: 8px;
    font-family: "Exo 2", sans-serif; font-weight: 500;
    font-size: 21px; color: var(--navy);
  }
</style>
</head>
<body>
<main class="flyer">
  <section class="header">
    <div class="header-blueprint" role="img" aria-label="Faint blueprint scaffolding line drawing across the header"></div>
    <svg class="header-notch" width="210" height="34" viewBox="0 0 210 34">
      <polygon points="0,0 210,0 210,32 32,32" fill="var(--white)"/>
    </svg>
    <div class="header-brand"><span class="brand-mark"></span>KERNO SOLUTIONS</div>
    <div class="tagline">
      <div class="lead">We are specialized in buying properties</div>
      <div class="sub">on which we develop and build constructions before selling them</div>
      <div class="tagline-rule"></div>
    </div>
  </section>

  <section class="letter">
    <p class="salute">Madame, Monsieur,</p>
    <p class="body">Ce courrier vous a été adressé, car votre propriété a attiré notre attention.<br>Nous souhaiterions discuter avec vous de son éventuel rachat par notre société.</p>
    <p class="body">En cas d’accord, nous vous assurons une décision rapide, un paiement garanti,<br>et zéro frais d’intermédiaire.</p>
    <p class="body">En attendant de vos nouvelles, nous restons à votre entière disposition pour tout renseignement.</p>
    <p class="closing">Salutations distinguées,</p>
    <p class="signature">L’équipe de Kerno Solutions</p>
  </section>

  <div class="footer-blueprint" role="img" aria-label="Faint blueprint scaffolding line drawing near the footer"></div>

  <svg class="footer-shapes" width="792" height="1120" viewBox="0 0 792 1120">
    <defs>
      <linearGradient id="bandFill" x1="0" y1="0" x2="1" y2="0">
        <stop offset="0" stop-color="var(--navy)"/>
        <stop offset="1" stop-color="var(--blue)"/>
      </linearGradient>
    </defs>
    <polygon points="0,951 195,812 195,932 0,1055" fill="var(--blue)"/>
    <polygon points="0,1040 170,951 792,951 792,972 675,1055 0,1055" fill="url(#bandFill)"/>
    <polygon points="740,1010 792,972 792,1055" fill="var(--pale)"/>
  </svg>

  <div class="footer-brand"><span class="brand-mark"></span>KERNO SOLUTIONS</div>

  <address class="contact" style="font-style:normal">
    <div class="company">Kerno Solutions sàrl</div>
    <div class="row">
      <svg viewBox="0 0 16 16"><path d="M8 1a5 5 0 0 0-5 5c0 4 5 9 5 9s5-5 5-9a5 5 0 0 0-5-5zm0 7a2 2 0 1 1 0-4 2 2 0 0 1 0 4z" fill="var(--white)"/></svg>
      <span>17 rue des Ateliers, L-3290 Bettembourg</span>
    </div>
    <div class="row">
      <svg viewBox="0 0 16 16"><rect x="1.5" y="3.5" width="13" height="9" fill="none" stroke="var(--white)" stroke-width="1.3"/><path d="M1.5 3.5 8 9l6.5-5.5" fill="none" stroke="var(--white)" stroke-width="1.3"/></svg>
      <span>info@kernosolutions-example.lu</span>
    </div>
    <div class="row">
      <svg viewBox="0 0 16 16"><path d="M4 1.5 6.5 4.5 5 6.5c.8 1.8 2.2 3.2 4 4l2-1.5 3 2.5-1.5 2.5C7.5 14 2 8.5 1.5 3z" fill="var(--white)"/></svg>
      <span>691 000 123</span>
    </div>
  </address>

  <div class="website">
    <svg width="20" height="20" viewBox="0 0 20 20"><circle cx="10" cy="10" r="8.5" fill="none" stroke="var(--navy)" stroke-width="1.6"/><ellipse cx="10" cy="10" rx="3.6" ry="8.5" fill="none" stroke="var(--navy)" stroke-width="1.4"/><line x1="1.5" y1="10" x2="18.5" y2="10" stroke="var(--navy)" stroke-width="1.4"/></svg>
    <span>WWW.KERNOSOLUTIONS-EXAMPLE.LU</span>
  </div>
</main>
</body>
</html>
```